Business Card Design Project

I need some business cards with the logo you did for us (attached)
I am looking for a coulourful yet serious business card

We do market research
on the back I want the logo

on the front my name : Corinne Valdessac
position : Manager
address : Brume Analytica Sarl - 27 Rue des tanneurs
1847 Glarency - Switzerland
corinne.valdessac@brumeanalytica.ch
Tel : +4122 934 07 58
Mob France :+33 671 42 8356
Mob Italy +39 347 520 8163

The tree of the logo could also be used alone

THE BACKGROUND COLOR ON THE FRONT HAS TO BE WHITE, ON THE BACK YU CAN TRY OHER COLOUR BUT HOMOGENEOUS (NOT EXPENSIVE TO PRINT)

Target Market(s)

multinational companies or other market research companies

Industry/Entity Type

Market Research

Requirements
Must have
• logo on the back
and all the info above

```html
<!DOCTYPE html>
<html lang="en">
<head>
<meta charset="utf-8">
<title>Brume Analytica – Business Cards</title>
<link rel="stylesheet" href="https://fonts.googleapis.com/css2?family=Arimo:wght@400&display=swap">
<style>
  :root {
    --backdrop: #ece7e1;
    --card: #ffffff;
    --crimson: #b01c4a;
    --maroon: #9a1f36;
    --green: #1f9a4c;
    --orange: #f2a33a;
    --magenta: #e0197d;
    --shadow: rgba(60, 40, 20, 0.22);
  }
  * { margin: 0; padding: 0; box-sizing: border-box; }
  html, body {
    width: 1200px;
    height: 1000px;
    overflow: hidden;
    background: var(--backdrop);
    font-family: "Arimo", Arial, sans-serif;
  }
  .canvas {
    position: relative;
    width: 1200px;
    height: 1000px;
  }
  .card {
    position: absolute;
    top: 355px;
    width: 500px;
    height: 290px;
    background: var(--card);
    box-shadow: 0 6px 18px var(--shadow), 0 1px 3px var(--shadow);
  }
  .card--back { left: 70px; }
  .card--front { left: 630px; }

  /* Back: brand name */
  .brand {
    position: absolute;
    left: 0;
    right: 0;
    top: 50%;
    transform: translateY(-50%);
    display: flex;
    align-items: center;
    justify-content: center;
    gap: 14px;
  }
  .brand__dot {
    width: 34px;
    height: 34px;
    border-radius: 50%;
    background: var(--crimson);
  }
  .brand__name {
    font-size: 40px;
    font-weight: 400;
    color: var(--crimson);
    letter-spacing: 0.5px;
  }

  /* Front: motif + details */
  .motif {
    position: absolute;
    left: 34px;
    top: 48px;
    width: 170px;
    height: 200px;
    border-radius: 8px;
    background: radial-gradient(circle at 45% 40%, #f5c84a 0%, #e35a9a 45%, #9bcb4f 80%, #ffffff 100%);
    opacity: 0.85;
  }
  .details {
    position: absolute;
    left: 226px;
    top: 44px;
    font-size: 12.5px;
    line-height: 1.35;
  }
  .details__name { font-size: 15px; color: var(--maroon); }
  .details__role { font-size: 14px; color: var(--maroon); margin-bottom: 20px; }
  .details__address { color: var(--green); margin-bottom: 20px; }
  .details__email { color: var(--orange); margin-bottom: 14px; }
  .details__phones { color: var(--magenta); }
</style>
</head>
<body>
<main class="canvas">
  <section class="card card--back" aria-label="Card back">
    <div class="brand">
      <span class="brand__dot"></span>
      <span class="brand__name">Brume Analytica</span>
    </div>
  </section>

  <section class="card card--front" aria-label="Card front">
    <div class="motif" role="img" aria-label="Colourful swirl tree motif"></div>
    <div class="details">
      <p class="details__name">Corinne Valdessac</p>
      <p class="details__role">Manager</p>
      <p class="details__address">Brume Analytica Sarl - 27 Rue des tanneurs<br>1847 Glarency - Switzerland</p>
      <p class="details__email">corinne.valdessac@brumeanalytica.ch</p>
      <p class="details__phones">tel : +4122 934 07 58<br>mob France : +33 671 42 8356<br>mob Italy +39 347 520 8163</p>
    </div>
  </section>
</main>
</body>
</html>
```